Design for schnapps bottle label "Sol Terrado"

Hi! On a small land lot we are producing our own Italian schnapps "Grappa". For the bottles we would like to modernize our current labes that you find below. The two cats looking at each other should remain, but updated and more modern. I am very much looking forward to your suggestions. Best, Joel

Target Market(s)

Schnapps bottle label

Requirements
Must have
• Cats should resemble the cats that are decorating the house entry (see attached), however, should have a more modern appearance.

Text elements should remain: "Grappa", "Sol Terrado", "Legnoso", "[Vintage Year], "Raccolta No", "Vol %"
Should not have
• Current ornament can be used, replaced or deleted (whatever looks best)

```html
<!DOCTYPE html>
<html lang="it">
<head>
<meta charset="utf-8">
<title>Grappa Sol Terrado – Label</title>
<link href="https://fonts.googleapis.com/css2?family=Libre+Caslon+Text:wght@400;700&display=swap" rel="stylesheet">
<style>
  :root {
    --canvas: #ffffff;
    --ink: #1c1c1c;
    --frame: #1a1a1a;
    --cutline: #d4d4d4;
    --paper: #ffffff;
    --ray: #e6e6e6;
    --cat: #3a3a3a;
    --ribbon: #c8151b;
    --ribbon-dark: #8e0c10;
    --ribbon-light: #e23a3a;
    --ribbon-text: #ffffff;
  }
  html, body {
    margin: 0;
    padding: 0;
    width: 1200px;
    height: 800px;
    overflow: hidden;
    background: var(--canvas);
  }
  .stage {
    width: 1200px;
    height: 800px;
    display: flex;
    align-items: center;
    justify-content: center;
  }
  .label {
    width: 440px;
    height: 620px;
    display: block;
  }
  .label-text {
    font-family: "Libre Caslon Text", "Times New Roman", serif;
    fill: var(--ink);
  }
  .label-title { font-size: 28px; font-weight: 700; letter-spacing: 0.5px; }
  .label-variety { font-size: 14px; font-weight: 400; }
  .label-year { font-size: 13px; font-weight: 400; }
  .label-meta { font-size: 9.5px; }
  .ribbon-name {
    font-family: "Libre Caslon Text", "Times New Roman", serif;
    font-size: 20px;
    font-weight: 700;
    fill: var(--ribbon-text);
  }
</style>
</head>
<body>
<main class="stage">
  <svg class="label" viewBox="110 140 220 310" xmlns="http://www.w3.org/2000/svg">
    <defs>
      <radialGradient id="paper-glow" cx="50%" cy="55%" r="60%">
        <stop offset="0%" stop-color="var(--paper)"/>
        <stop offset="100%" stop-color="var(--ray)"/>
      </radialGradient>
      <linearGradient id="ribbon-shade" x1="0" y1="0" x2="0" y2="1">
        <stop offset="0%" stop-color="var(--ribbon-light)"/>
        <stop offset="55%" stop-color="var(--ribbon)"/>
        <stop offset="100%" stop-color="var(--ribbon-dark)"/>
      </linearGradient>
    </defs>

    <path class="label-cutline" fill="var(--paper)" stroke="var(--cutline)" stroke-width="1"
      d="M138 146 H300 Q314 146 314 160 V250 Q322 290 318 340 L316 372 V432 Q316 442 304 442 H136 Q124 442 124 432 V372 L120 340 Q118 290 126 250 V160 Q126 146 138 146 Z"/>

    <rect class="label-panel" x="130" y="152" width="178" height="284" rx="10" fill="url(#paper-glow)" stroke="var(--frame)" stroke-width="2.5"/>

    <ellipse class="label-medallion" cx="219" cy="302" rx="88" ry="76" fill="var(--paper)" stroke="var(--frame)" stroke-width="2.5"/>

    <text class="label-text label-title" x="219" y="204" text-anchor="middle">GRAPPA</text>

    <rect class="label-flourish" x="207" y="243" width="24" height="3" rx="1.5" fill="var(--cat)" role="img" aria-label="Small decorative flourish"/>

    <text class="label-text label-variety" x="219" y="269" text-anchor="middle">LEGNOSO</text>
    <text class="label-text label-year" x="219" y="287" text-anchor="middle">2015</text>

    <rect class="label-cats" x="138" y="295" width="162" height="40" rx="18" fill="var(--cat)" role="img" aria-label="Two stylised black cats stretching and facing each other"/>

    <g class="label-ribbon">
      <path fill="var(--ribbon-dark)" d="M122 342 L140 340 L142 372 L126 376 L132 360 Z"/>
      <path fill="var(--ribbon-dark)" d="M316 336 L298 338 L296 370 L312 372 L308 354 Z"/>
      <path fill="url(#ribbon-shade)" d="M134 338 Q220 368 304 334 L306 366 Q220 398 136 370 Z"/>
      <text class="ribbon-name" x="220" y="374" text-anchor="middle" textLength="144" lengthAdjust="spacingAndGlyphs">SOL TERRADO</text>
    </g>

    <text class="label-text label-meta" x="144" y="421">Raccolta No</text>
    <text class="label-text label-meta" x="292" y="421" text-anchor="end">Vol %</text>
  </svg>
</main>
</body>
</html>
```